Brindlecove Flood Restoration needing website

Hi Team

We are looking for a 4 or 5 page website containing
1: Home
2: Services
3: Gallery
4: Equipment Hire
5 Contact Us

Would want the front page to be a big call to action. Someones house has just flooded...they're highly stressed and we just want to let them know straight away that we can assist them

Some call to action would be great.

"Wet Carpets??"

"Washing machine just overflowed??"

"Burst pipe?"

"We're here to help!!"

Would be wanting a scrolling banner type homepage with images of flooded houses, heavy rain, a mother in shock that the house has been flooded by an overflowing washing machine, someone taking an emergency call with text saying that we are there to take your call 24/7 365 days a year

Target Market(s)

insurance companies and home owners

Industry/Entity Type

Hire

Coding

Coded - Design and coding required

Number of Pages Required

5+ page

Requirements
Must have
• 24/7 emergency contact number on home page (0498215763)
• 4 photos on banner on home page
• Equipment Hire Page should include images and brief description of these 3 products
• http://www.ptkdirect.example.com.au/prod458.htm
• http://www.gustline-gear.example.com.au/product/mistral-breeze-fan/
• http://www.vendrasuck.example.com.au/carpet/carpet-extractor-harrier-xv-x-vi-x-vii
• SERVICES OFFERED ARE:
• 24/7 Emergnecy Flood Restoration
• Insurance Claims
• Structural Drying
• Sub Floor Drying
• Supply and installation of drying equipment
• Professional Carpet and underlay installation
Nice to have
• Some other websites we like
• www.kelbyleakfixers.example.com.au
• www.summitrecoverywashing.example.com.au/flood-water-damage-restoration
• http://www.pelhamrecovery.example.com.au/
• http://www.dampfixnational.example.com.au/
Should not have
• not looking for an all white background.

```html
<!DOCTYPE html>
<html lang="en">
<head>
<meta charset="utf-8">
<title>Brindlecove Flood Restoration</title>
<link rel="stylesheet" href="https://fonts.googleapis.com/css2?family=Cinzel:wght@400;700&family=Open+Sans:ital,wght@0,400;0,600;0,700;1,400&display=swap">
<style>
:root{
  --blue:#1b7bc0;
  --blue-dark:#146aa8;
  --red:#e8434f;
  --red-dark:#d9363f;
  --ink:#222;
  --grey-text:#666;
  --light:#efefef;
  --footer:#2c2c2c;
  --footer-bar:#232323;
  --white:#fff;
}
*{box-sizing:border-box;margin:0;padding:0}
html,body{width:1200px;height:2439px;overflow:hidden}
body{position:relative;font-family:"Open Sans",Arial,sans-serif;color:var(--ink);background:var(--white)}
.abs{position:absolute}
.serif{font-family:"Cinzel",Georgia,serif}

/* header */
.site-header{position:absolute;left:0;top:0;width:1200px;height:96px;background:var(--white);border-top:5px solid var(--blue)}
.brand{position:absolute;left:80px;top:22px;display:flex;align-items:center;gap:12px}
.brand-dot{width:44px;height:44px;border-radius:50%;background:var(--blue)}
.brand-name{font-family:"Cinzel",Georgia,serif;font-weight:700;color:var(--blue);font-size:22px;line-height:1.05;width:260px}
.top-contact{position:absolute;right:100px;top:14px;display:flex;align-items:center;gap:10px;font-size:13px;font-weight:700}
.top-contact .num{color:var(--red);font-size:20px;font-weight:600}
.phone-ring{width:30px;height:30px;border:2px solid var(--blue);border-radius:50%;display:flex;align-items:center;justify-content:center}
.main-nav{position:absolute;top:62px;left:527px;display:flex;gap:0;font-size:14px;font-weight:600}
.main-nav a{color:var(--ink);text-decoration:none;position:absolute;white-space:nowrap}
.main-nav a.active{color:var(--red)}

/* hero */
.hero{position:absolute;left:0;top:96px;width:1200px;height:398px;background:linear-gradient(180deg,#8e9194 0%,#6d7073 45%,#55585a 100%)}
.hero-title{position:absolute;top:92px;width:100%;text-align:center;color:var(--white);font-size:50px;letter-spacing:1px;text-shadow:0 2px 4px rgba(0,0,0,.5)}
.hero-sub{position:absolute;top:164px;left:250px;width:700px;text-align:center;color:var(--white);font-size:17px;line-height:28px;text-shadow:0 1px 3px rgba(0,0,0,.6)}
.btn-info{position:absolute;left:359px;top:242px;width:215px;height:46px;background:var(--red);border:2px solid var(--white);color:var(--white);font-weight:700;font-size:15px;display:flex;align-items:center;justify-content:center}
.hero-or{position:absolute;left:598px;top:256px;color:var(--white);font-weight:700;font-size:14px}
.hero-contact{position:absolute;left:645px;top:238px;color:var(--white)}
.hero-contact small{display:block;font-size:12px;font-weight:600}
.hero-contact strong{display:block;font-size:32px;font-weight:600;line-height:38px}
.slider-dots{position:absolute;left:517px;top:349px;display:flex;gap:8px}
.slider-dots span{width:36px;height:5px;background:var(--white);border-radius:3px}
.slider-dots span.on{background:var(--blue)}

/* welcome */
.welcome{position:absolute;left:0;top:494px;width:1200px;height:392px;background:var(--light)}
.welcome h2{position:absolute;left:98px;top:48px;font-size:26px;font-weight:400;color:var(--ink)}
.welcome .copy{position:absolute;left:98px;top:96px;width:655px;font-size:12.5px;line-height:23.5px;color:var(--grey-text)}
.welcome .copy p+p{margin-top:24px}
.read-more{color:var(--red);font-weight:700;font-size:12px}
.welcome .read-more{position:absolute;left:98px;top:328px}
.service-card{position:absolute;left:795px;top:43px;width:306px;height:304px;background:var(--white);border:1px solid #ddd;box-shadow:0 10px 14px -10px rgba(0,0,0,.35);text-align:center}
.badge{position:absolute;left:83px;top:16px;width:140px;height:114px;border-radius:8px;background:linear-gradient(135deg,#d9e8f5,#f6d6d8)}
.service-card h3{position:absolute;top:138px;width:100%;font-size:19px;font-weight:400}
.service-card p{position:absolute;top:174px;left:28px;width:250px;font-size:12px;line-height:19px;color:var(--grey-text)}
.service-card .read-more{position:absolute;top:262px;left:0;width:100%}

/* services */
.services{position:absolute;left:0;top:886px;width:1200px;height:560px;background:var(--blue)}
.section-title{position:absolute;width:100%;text-align:center;font-size:23px;font-weight:400;color:var(--white)}
.section-sub{position:absolute;left:250px;width:700px;text-align:center;font-size:12.5px;line-height:23px;color:var(--white)}
.services .section-title{top:40px}
.services .section-sub{top:84px}
.tile{position:absolute;top:163px;width:234px;height:346px;background:var(--white);border:3px solid var(--white);box-shadow:0 12px 12px -10px rgba(0,0,0,.4);overflow:hidden}
.tile-photo{width:100%;height:158px}
.tile h4{margin:22px 14px 0;font-family:"Cinzel",Georgia,serif;font-size:16px;font-weight:700}
.tile p{margin:10px 14px 0;font-size:12px;line-height:20px;color:var(--grey-text)}
.tile-corner{position:absolute;right:0;bottom:0;width:48px;height:48px}

/* why */
.why{position:absolute;left:0;top:1446px;width:1200px;height:424px;background:linear-gradient(135deg,var(--red) 0%,var(--red-dark) 100%)}
.why .section-title{top:46px}
.why .section-sub{top:90px}
.feature{position:absolute;top:175px;width:240px;text-align:center;color:var(--white)}
.feature-ring{width:114px;height:114px;margin:0 auto;border:4px solid var(--white);border-radius:50%;display:flex;align-items:center;justify-content:center}
.feature h5{margin-top:20px;font-family:"Cinzel",Georgia,serif;font-size:18px;font-weight:400}
.feature p{margin-top:6px;font-size:12px;line-height:21px}

/* testimonials */
.testimonials{position:absolute;left:0;top:1870px;width:1200px;height:278px;background:var(--white)}
.testimonials h2{position:absolute;top:44px;width:100%;text-align:center;font-size:23px;font-weight:400}
.quote-bubble{position:absolute;left:146px;top:103px;width:112px;height:112px;border-radius:50%;background:#e6e6e6;color:#cfcfcf;font-family:Georgia,serif;font-size:90px;line-height:140px;padding-left:18px}
.client-photo{position:absolute;left:220px;top:103px;width:112px;height:112px;border-radius:50%;border:4px solid var(--white);background:linear-gradient(160deg,#cfd6dc,#5b6470)}
.quote{position:absolute;left:361px;top:104px;width:720px;font-size:14px;line-height:27.5px;font-style:italic;color:var(--grey-text)}
.client-name{position:absolute;left:361px;top:200px;font-size:14px;font-weight:700;color:var(--red)}
.arrow{position:absolute;top:147px}

/* footer */
.site-footer{position:absolute;left:0;top:2148px;width:1200px;height:237px;background:var(--footer);color:#ddd}
.footer-brand{position:absolute;left:85px;top:86px;display:flex;align-items:center;gap:12px}
.footer-brand .brand-dot{background:var(--white);width:40px;height:40px}
.footer-brand .brand-name{color:var(--white);font-size:20px;width:280px}
.footer-col{position:absolute;top:30px;font-size:12px;line-height:27.5px}
.footer-col h6{font-family:"Cinzel",Georgia,serif;font-size:16px;font-weight:400;color:var(--white);line-height:20px;margin-bottom:12px}
.footer-col a{color:#ddd;text-decoration:none;display:block}
.newsletter p{line-height:20px}
.email-field{margin-top:12px;width:254px;height:35px;background:var(--white);color:#999;font-size:11px;padding:0 14px;line-height:35px}
.btn-subscribe{margin-top:14px;width:86px;height:31px;background:var(--red);color:var(--white);font-size:11px;font-weight:700;line-height:31px;text-align:center}
.contact-line{display:flex;gap:14px;align-items:flex-start;line-height:20px;margin-bottom:14px}
.contact-line svg{flex:none;margin-top:3px}
.contact-line u{color:#ddd}
.footer-bar{position:absolute;left:0;top:2385px;width:1200px;height:54px;background:var(--footer-bar);border-top:1px solid #3a3a3a}
.footer-bar p{position:absolute;left:98px;top:18px;font-size:12px;color:#ccc}
.social{position:absolute;right:99px;top:17px;display:flex;gap:12px}
.social span{width:18px;height:18px;border-radius:50%;background:#ddd}
</style>
</head>
<body>

<header class="site-header">
  <div class="brand"><span class="brand-dot"></span><span class="brand-name">Brindlecove Flood Restoration</span></div>
  <div class="top-contact">
    <span class="phone-ring"><svg width="14" height="14" viewBox="0 0 24 24"><path fill="#1b7bc0" d="M6.6 10.8a15.1 15.1 0 0 0 6.6 6.6l2.2-2.2a1 1 0 0 1 1-.25 11.4 11.4 0 0 0 3.6.57 1 1 0 0 1 1 1V20a1 1 0 0 1-1 1A17 17 0 0 1 3 4a1 1 0 0 1 1-1h3.5a1 1 0 0 1 1 1c0 1.25.2 2.45.57 3.57a1 1 0 0 1-.25 1z"/></svg></span>
    <span>24/7 EMERGENCY CONTACT :</span><span class="num">(0498215763)</span>
  </div>
  <nav class="main-nav">
    <a class="active" style="left:0">HOME</a>
    <a style="left:78px">SERVICES</a>
    <a style="left:178px">GALLERY</a>
    <a style="left:276px">EQUIPMENT HIRE</a>
    <a style="left:435px">CONTACT US</a>
    <a style="left:560px;top:1px"><svg width="14" height="14" viewBox="0 0 24 24"><circle cx="10" cy="10" r="7" fill="none" stroke="#222" stroke-width="3"/><path d="M15 15l7 7" stroke="#222" stroke-width="3"/></svg></a>
  </nav>
</header>

<section class="hero" role="img" aria-label="Banner photo: heavy rain falling on a flooded street">
  <h1 class="hero-title serif">WE'RE HERE TO HELP!!</h1>
  <p class="hero-sub">At vero eos et accusamus et iusto odio dignissimos ducimus qui blanditiis praesentium voluptatum deleniti atque corrupti quos dolo</p>
  <div class="btn-info">GET MORE INFO &gt;&gt;</div>
  <span class="hero-or">OR</span>
  <div class="hero-contact"><small>24/7 EMERGENCY CONTACT :</small><strong>(0498215763)</strong></div>
  <div class="slider-dots"><span class="on"></span><span></span><span></span><span></span></div>
</section>

<section class="welcome">
  <h2 class="serif">Welcome to Brindlecove Flood Restoration</h2>
  <div class="copy">
    <p>At vero eos et accusamus et iusto odio dignissimos ducimus qui blanditiis praesentium voluptatum deleniti atque corrupti quos dolores et quas molestias excepturi sint occaecati cupiditate non provident, similique sunt in culpa qui officia deserunt mollitia animi, id est laborum et dolorum fuga. Et harum quidem rerum facilis est et expedita distinctio num solut nobis est eligendi optio cumque nihil impedit quo minus id quod maxime.</p>
    <p>Placeat facere possimus, omnis voluptas assumenda est, omnis dolor repellendus. Temporibus autem quibusdam et aut officiis debitis aut rerum necessitatibus saepe eveniet ut et voluptates rep imilique sunt in culpa qui officia deserunt mollitia animi, id est laborum et dolorum fuga. Et harum quidem rerum facilis est et expedita distinctio. Nam libero tempore, cum soluta nobis est eligendi optio cumque nihil.</p>
  </div>
  <span class="read-more">READ MORE &gt;&gt;</span>
  <div class="service-card">
    <div class="badge" role="img" aria-label="24/7 emergency service badge"></div>
    <h3 class="serif">24/7 Emergency Service</h3>
    <p>At vero eos et accusamus et iusto odio dignissimos ducimus qui blanditiis praesentium voluptatum deleniti atque cor .</p>
    <span class="read-more">READ MORE &gt;&gt;</span>
  </div>
</section>

<section class="services">
  <h2 class="section-title serif">Our Services</h2>
  <p class="section-sub">Nemo enim ipsam voluptatem quia voluptas sit aspernatur aut odit aut fugit, sed quia consequuntur magni dolores eos qui ratione voluptatem sequi nesciunt, qui dolorem ipsum quia dolor sit.</p>

  <article class="tile" style="left:99px">
    <div class="tile-photo" role="img" aria-label="Photo: flooded modern kitchen" style="background:linear-gradient(180deg,#d8dde2,#5f7688)"></div>
    <h4>Finibus Bonorum etm</h4>
    <p>Nam libero tempore, cum solutanob is est eligendi optio cumque nihil ipedit quo minus id quod maxime placeat facere possimus..</p>
    <svg class="tile-corner" viewBox="0 0 48 48"><path d="M48 0V48H0Z" fill="#e8434f"/><path d="M34 31v10M29 36h10" stroke="#fff" stroke-width="2.5"/></svg>
  </article>
  <article class="tile" style="left:356px">
    <div class="tile-photo" role="img" aria-label="Photo: carpet cleaning machine on wet floor" style="background:linear-gradient(180deg,#8a8d90,#4d5256)"></div>
    <h4>Finibus Bonorum etm</h4>
    <p>Nam libero tempore, cum solutanob is est eligendi optio cumque nihil ipedit quo minus id quod maxime placeat facere possimus..</p>
    <svg class="tile-corner" viewBox="0 0 48 48"><path d="M48 0V48H0Z" fill="#e8434f"/><path d="M34 31v10M29 36h10" stroke="#fff" stroke-width="2.5"/></svg>
  </article>
  <article class="tile" style="left:611px">
    <div class="tile-photo" role="img" aria-label="Photo: overflowing washing machine in a laundry" style="background:linear-gradient(180deg,#4f6f74,#2f4a52)"></div>
    <h4>Finibus Bonorum etm</h4>
    <p>Nam libero tempore, cum solutanob is est eligendi optio cumque nihil ipedit quo minus id quod maxime placeat facere possimus..</p>
    <svg class="tile-corner" viewBox="0 0 48 48"><path d="M48 0V48H0Z" fill="#e8434f"/><path d="M34 31v10M29 36h10" stroke="#fff" stroke-width="2.5"/></svg>
  </article>
  <article class="tile" style="left:867px">
    <div class="tile-photo" role="img" aria-label="Photo: water pouring into a flooded room" style="background:linear-gradient(180deg,#5a4536,#2e2620)"></div>
    <h4>Finibus Bonorum etm</h4>
    <p>Nam libero tempore, cum solutanob is est eligendi optio cumque nihil ipedit quo minus id quod maxime placeat facere possimus..</p>
    <svg class="tile-corner" viewBox="0 0 48 48"><path d="M48 0V48H0Z" fill="#e8434f"/><path d="M34 31v10M29 36h10" stroke="#fff" stroke-width="2.5"/></svg>
  </article>
</section>

<section class="why">
  <h2 class="section-title serif">Why Choose Us</h2>
  <p class="section-sub">Nemo enim ipsam voluptatem quia voluptas sit aspernatur aut odit aut fugit, sed quia consequuntur magni dolores eos qui ratione voluptatem sequi nesciunt, qui dolorem ipsum quia dolor sit.</p>

  <div class="feature" style="left:90px">
    <div class="feature-ring"><svg width="54" height="54" viewBox="0 0 24 24"><path fill="#fff" d="M2 10h4v12H2zM8 21V10l5-8c1.4 0 2.4 1.2 2 2.6L14 9h6.5a2 2 0 0 1 2 2.3l-1.4 8A2 2 0 0 1 19 21z"/></svg></div>
    <h5>Qualified</h5>
    <p>At vero eos et accusamus et iusto odio dignissimos ducimus qui bla</p>
  </div>
  <div class="feature" style="left:350px">
    <div class="feature-ring"><svg width="58" height="58" viewBox="0 0 24 24"><path fill="#fff" d="M12 1.5l3.1 6.8 7.4.8-5.5 5 1.6 7.3L12 17.7l-6.6 3.7L7 14.1l-5.5-5 7.4-.8z"/></svg></div>
    <h5>Experienced</h5>
    <p>At vero eos et accusamus et iusto odio dignissimos ducimus qui bla</p>
  </div>
  <div class="feature" style="left:612px">
    <div class="feature-ring"><svg width="54" height="54" viewBox="0 0 24 24"><path fill="#fff" d="M22 2L1 10.5l6.5 2.5L18 5l-8.5 9.5V22l3.6-4.6 4.9 3.1z"/></svg></div>
    <h5>Fast 24/7 Service</h5>
    <p>At vero eos et accusamus et iusto odio dignissimos ducimus qui bla</p>
  </div>
  <div class="feature" style="left:872px">
    <div class="feature-ring"><svg width="58" height="58" viewBox="0 0 24 24"><g fill="none" stroke="#fff" stroke-width="2.2"><circle cx="9" cy="14" r="3.2"/><path d="M9 7.5v2M9 18.5v2M2.5 14h2M13.5 14h2M4.4 9.4l1.4 1.4M12.2 17.2l1.4 1.4M4.4 18.6l1.4-1.4M12.2 10.8l1.4-1.4"/><circle cx="17.5" cy="6.5" r="2"/><path d="M17.5 2.5v1.5M17.5 9v1.5M13.5 6.5H15M20 6.5h1.5"/></g></svg></div>
    <h5>Latest Equipment</h5>
    <p>At vero eos et accusamus et iusto odio dignissimos ducimus qui bla</p>
  </div>
</section>

<section class="testimonials">
  <h2 class="serif">Client Testimonials</h2>
  <svg class="arrow" style="left:98px" width="14" height="24" viewBox="0 0 14 24"><path d="M12 2L3 12l9 10" fill="none" stroke="#999" stroke-width="2"/></svg>
  <svg class="arrow" style="left:1088px" width="14" height="24" viewBox="0 0 14 24"><path d="M2 2l9 10-9 10" fill="none" stroke="#999" stroke-width="2"/></svg>
  <div class="quote-bubble">&ldquo;</div>
  <div class="client-photo" role="img" aria-label="Client portrait"></div>
  <p class="quote">It is a long established fact that a reader will be distracted by the readable content of a page when looking at its layout. The point of using Lorem Ipsum is that it has a more-or-less normal distribution of letters, as opposed to using 'Content here, content here', making it look like readable English.</p>
  <span class="client-name">- MARCUS TELLWOOD</span>
</section>

<footer class="site-footer">
  <div class="footer-brand"><span class="brand-dot"></span><span class="brand-name">Brindlecove Flood Restoration</span></div>
  <div class="footer-col" style="left:442px">
    <h6>Information</h6>
    <a>Home</a><a>Services</a><a>Gallery</a><a>Equipment hire</a><a>Contact us</a>
  </div>
  <div class="footer-col newsletter" style="left:595px">
    <h6>Newsletter Subscription</h6>
    <p>Register Your Email Address to get<br>Information about us</p>
    <div class="email-field">Email Address</div>
    <div class="btn-subscribe">SUBSCRIBE</div>
  </div>
  <div class="footer-col" style="left:891px;width:240px">
    <h6>Contact Us</h6>
    <div class="contact-line"><svg width="11" height="14" viewBox="0 0 12 16"><path fill="#ddd" d="M6 0a6 6 0 0 0-6 6c0 4.5 6 10 6 10s6-5.5 6-10a6 6 0 0 0-6-6zm0 8.5A2.5 2.5 0 1 1 6 3.5a2.5 2.5 0 0 1 0 5z"/></svg><span>27 Harlow Quay Road<br>Dunmore Bay, PA 17408</span></div>
    <div class="contact-line"><svg width="13" height="13" viewBox="0 0 24 24"><path fill="#ddd" d="M6.6 10.8a15.1 15.1 0 0 0 6.6 6.6l2.2-2.2a1 1 0 0 1 1-.25 11.4 11.4 0 0 0 3.6.57 1 1 0 0 1 1 1V20a1 1 0 0 1-1 1A17 17 0 0 1 3 4a1 1 0 0 1 1-1h3.5a1 1 0 0 1 1 1c0 1.25.2 2.45.57 3.57a1 1 0 0 1-.25 1z"/></svg><span>0498215763</span></div>
    <div class="contact-line"><svg width="14" height="11" viewBox="0 0 16 12"><path fill="#ddd" d="M0 0h16v12H0z"/><path d="M0 0l8 6 8-6" fill="none" stroke="#2c2c2c" stroke-width="1.5"/></svg><u style="font-size:11px">info@brindlecovefloodrestoration.example.com</u></div>
  </div>
</footer>
<div class="footer-bar">
  <p>&copy; 2016, Brindlecove Flood Restoration. All rights reserved.</p>
  <div class="social"><span></span><span></span><span></span></div>
</div>

</body>
</html>
```